Real Estate Investor needs awesome business card design

I invest in real estate, focused on multi-family properties, and I need a business card to hand out to potential partners. I prefer simple, clean designs, but it needs to stand out, so I'd like there to be a bit of red in the design as well.

It should include this information:

Front
Calder Whitby
Real Estate Investor
Direct phone: 501-555-0187
Email: calderjwhitby@mailbox-example.net
Headshot (Picture), I've uploaded a few, just pick the one you think looks best with your design. You can remove the background from the headshot image if it looks better.

Back
The back of the card's design should flow and be congruent with the front. On the back I want to put an inspirational quote or question. There will be different ones depending on the card, so I'll need the original file so I can edit it in the end.

For now, use “The Pessimist Sees Difficulty In Every Opportunity. The Optimist Sees The Opportunity In Every Difficulty.” -Edmund Halvorsen

Target Market(s)

Investors

Industry/Entity Type

Real Estate

Contact Information for Business Card

Front
Calder Whitby
Real Estate Investor

Back
The back of the card's design should flow and be congruent with the front. On the back I want to put an inspirational quote or question. There will be different ones depending on the card, so I'll need the original file so I can edit it in the end. I've uploaded some EXAMPLES of business cards with quotes on them. Don't copy but feel free to use them as inspiration.

The design will be printed on "ZAP sized" business cards
1039 x 697 pixels
with rounded corners

Font styles to use
Serif
Decorative
Script

Colors
ec1f27

Requirements
Must have
• Headshot, name, and other information in it.
• 1039 x 697 pixels
• Rounded corners
• Clean design that pops. I'm open to see any color background, including black.
• Headshots can be located here: https://www.filecrate-example.com/sh/8kx2vq71ld0pa3z/BQQTXL7mrrf9eT3Kq0HhgkLm2b?dl=0
Nice to have
• It would be awesome if the design included a personal signature or monogram, but if not I'll get a personal logo developed later and the card redesigned if I think it needs it.
Should not have
• Cluttered design

```html
<!DOCTYPE html>
<html lang="en">
<head>
<meta charset="utf-8">
<title>Calder Whitby – Real Estate Investor</title>
<link rel="stylesheet" href="https://fonts.googleapis.com/css2?family=Aldrich&family=Didact+Gothic&display=swap">
<style>
  :root {
    --page: #ffffff;
    --card-bg: #0d0d0d;
    --card-glow: #2a2a2a;
    --photo-light: #4a4a4a;
    --photo-mid: #262626;
    --photo-dark: #101010;
    --accent-red: #ec1f27;
    --band: rgba(92, 92, 92, 0.88);
    --band-text: #f4f4f4;
  }
  * { box-sizing: border-box; margin: 0; padding: 0; }
  html, body {
    width: 805px;
    height: 1200px;
    overflow: hidden;
    background: var(--page);
  }
  .card {
    position: relative;
    width: 805px;
    height: 1200px;
    border-radius: 38px;
    overflow: hidden;
    background: radial-gradient(ellipse at 62% 30%, var(--card-glow) 0%, var(--card-bg) 62%);
  }
  .headshot {
    position: absolute;
    left: 205px;
    top: 60px;
    right: 0;
    bottom: 0;
    background:
      radial-gradient(ellipse 34% 22% at 57% 20%, var(--photo-light) 0%, transparent 100%),
      linear-gradient(180deg, var(--photo-mid) 0%, var(--photo-dark) 100%);
    border-radius: 220px 220px 0 0;
    opacity: 0.9;
  }
  .name {
    position: absolute;
    left: 22px;
    top: 1150px;
    transform: rotate(-90deg);
    transform-origin: 0 0;
    font-family: "Aldrich", sans-serif;
    font-size: 78px;
    line-height: 80px;
    letter-spacing: 26px;
    text-transform: uppercase;
    white-space: nowrap;
    color: var(--accent-red);
    text-shadow: 0 0 3px rgba(236, 31, 39, 0.6);
  }
  .info-band {
    position: absolute;
    height: 62px;
    background: var(--band);
    transform: rotate(-18deg);
    transform-origin: 0 100%;
    display: flex;
    align-items: center;
    padding-left: 22px;
    font-family: "Didact Gothic", sans-serif;
    color: var(--band-text);
    white-space: nowrap;
  }
  .info-band--title { left: 373px; top: 728px; width: 560px; font-size: 32px; letter-spacing: 1px; }
  .info-band--phone { left: 282px; top: 903px; width: 640px; font-size: 31px; }
  .info-band--email { left: 258px; top: 1102px; width: 720px; font-size: 24px; }
</style>
</head>
<body>
  <div class="card">
    <div class="headshot" role="img" aria-label="Black and white headshot of Calder Whitby in a dark suit"></div>
    <h1 class="name">Calder Whitby</h1>
    <div class="info-band info-band--title">Real Estate Investor</div>
    <div class="info-band info-band--phone">Direct phone: 501-555-0187</div>
    <div class="info-band info-band--email">Email: calderjwhitby@mailbox-example.net</div>
  </div>
</body>
</html>
```